Harborline Capital Inc. Investor Presentation

We would like a PowerPoint presentation to attract prospective investors. It needs to look extremely professional since we are a financial lending institution, and seeking capital investors. We specialize in Private Lending with Mortgage Backed Securities, both Residential and Commercial properties.

```html
<!DOCTYPE html>
<html lang="en">
<head>
<meta charset="utf-8">
<title>Harborline Capital Inc. — Investor Presentation</title>
<link href="https://fonts.googleapis.com/css2?family=Montserrat:wght@300;400;500;600;700&display=swap" rel="stylesheet">
<style>
:root{
  --bg:#cfced1;
  --red:#e0242b;
  --ink:#25272b;
  --text:#2b2b2b;
  --white:#ffffff;
  --muted:#6b6d72;
}
*{margin:0;padding:0;box-sizing:border-box}
html,body{width:1200px;height:994px;overflow:hidden;background:var(--bg)}
body{font-family:'Montserrat',sans-serif;color:var(--text);position:relative}
.slide{position:absolute;width:303px;height:170px;background:var(--white);overflow:hidden;box-shadow:2px 3px 5px rgba(0,0,0,.28)}
.abs{position:absolute}
.photo{position:absolute}
.title-red{color:var(--red);font-weight:700;font-size:8px;line-height:9.5px;text-transform:uppercase}
.body{font-size:4.6px;line-height:6px;color:var(--text)}
.body.light{color:var(--white)}
.logo-mini{position:absolute;right:24px;bottom:8px;font-size:4px;font-weight:600;color:var(--red)}
.dot{position:absolute;width:13px;height:13px;border-radius:50%;display:flex;align-items:center;justify-content:center}
.dot.red{background:var(--red)}
.dot.dark{background:var(--ink)}
.dot svg{width:7px;height:7px}
.tick{position:absolute;width:5px;height:5px;border-radius:50%;background:var(--red)}
.item-text{position:absolute;font-size:3.8px;line-height:5px;color:var(--text)}
</style>
</head>
<body>

<!-- Cover -->
<section class="slide" style="left:474px;top:87px">
  <div class="abs" style="left:0;top:29px;width:128px;height:85px;background:var(--ink)"></div>
  <h1 class="abs" style="left:16px;top:54px;font-size:12px;line-height:14px;font-weight:600;color:var(--white)"><span style="color:var(--red)">2022</span> Company<br>Presentation</h1>
  <div class="abs" style="left:14px;top:148px;font-size:15px;font-weight:500;color:var(--red);line-height:15px">LOGO</div>
  <div class="photo" role="img" aria-label="Smiling businessman on the phone at a laptop in a bright office" style="left:128px;top:0;width:175px;height:170px;background:linear-gradient(135deg,#c9b9a4,#8d7a66 55%,#e9e2d8)"></div>
</section>

<!-- Slide: city towers -->
<section class="slide" style="left:95px;top:290px">
  <div class="photo" role="img" aria-label="Skyscrapers seen from below against a pale blue sky" style="left:0;top:0;width:233px;height:170px;background:linear-gradient(160deg,#8f9bb8,#a7aed0 45%,#6b5d66)"></div>
  <div class="abs" style="left:128px;top:55px;width:162px;height:81px;background:var(--red)"></div>
  <div class="abs" style="left:162px;top:49px;width:95px;height:20px;background:var(--ink);color:var(--white);font-size:7.5px;font-weight:300;display:flex;align-items:center;justify-content:center">GRAPHIC 02</div>
  <p class="body light abs" style="left:136px;top:80px;width:146px;text-align:center;font-size:4.4px;line-height:6px">Lorem ipsum dolor sit amet, consectetuer adipiscing elit, sed diam nonummy nibh euismod tincidunt ut laoreet dolore magna aliquam erat volutpat. Ut wisi enim ad minim veniam, quis nostrud exerci tation ullamcorper suscipit lobortis nisl ut aliquip ex ea commodo consequat. Duis autem vel eum iriure dolor in hendrerit in vul-</p>
  <div class="logo-mini" style="right:15px">LOGO</div>
</section>

<!-- Slide: digital network -->
<section class="slide" style="left:474px;top:290px">
  <div class="photo" role="img" aria-label="Hand touching a tablet with a glowing network globe" style="left:0;top:0;width:71px;height:125px;background:linear-gradient(160deg,#8d8f99,#c9c9cf 50%,#4a64a8)"></div>
  <div class="photo" role="img" aria-label="Finger tapping a tablet under a digital network sphere" style="left:74px;top:31px;width:95px;height:139px;background:linear-gradient(160deg,#5c5d66,#b9bac0 50%,#7f8aa8)"></div>
  <div class="title-red abs" style="left:180px;top:35px">GRAPHIC 02</div>
  <p class="body abs" style="left:180px;top:58px;width:98px">Lorem ipsum dolor sit amet, consectetuer adipiscing elit, sed diam nonummy nibh euismod tincidunt ut laoreet dolore magna aliquam erat volutpat. Ut wisi enim ad minim veniam, quis nostrud exerci tation ullamcorper suscipit lobortis nisl ut aliquip ex ea commodo consequat. Duis autem vel eum iriure dolor in hendrerit in vulputate velit esse molestie consequat, vel</p>
  <div class="logo-mini">LOGO</div>
</section>

<!-- Slide: meeting -->
<section class="slide" style="left:829px;top:290px">
  <div class="abs" style="left:0;top:0;width:70px;height:132px;background:var(--ink)"></div>
  <div class="photo" role="img" aria-label="Colleagues taking notes around a wooden meeting table" style="left:28px;top:31px;width:140px;height:139px;background:linear-gradient(150deg,#6c7c94,#9b9790 45%,#4a3b33)"></div>
  <div class="title-red abs" style="left:181px;top:35px">This is a header<br>This is a header</div>
  <p class="body abs" style="left:181px;top:58px;width:98px">Lorem ipsum dolor sit amet, consectetuer adipiscing elit, sed diam nonummy nibh euismod tincidunt ut laoreet dolore magna aliquam erat volutpat. Ut wisi enim ad minim veniam, quis nostrud exerci tation ullamcorper suscipit lobortis nisl ut aliquip ex ea commodo consequat. Duis autem vel eum iriure dolor in hendrerit in vulputate velit esse molestie consequat, vel</p>
  <div class="logo-mini">LOGO</div>
</section>

<!-- Slide: growth list -->
<section class="slide" style="left:95px;top:497px">
  <div class="photo" role="img" aria-label="Seedlings growing from rising stacks of gold coins" style="left:134px;top:0;width:220px;height:190px;border-radius:50%;background:radial-gradient(circle at 60% 40%,#c6dd8f,#7faa4f 55%,#b79d57)"></div>
  <div class="title-red abs" style="left:14px;top:8px">Graphic 02</div>
  <p class="body abs" style="left:15px;top:22px;width:92px;font-size:5px">Lorem ipsum dolor sit amet, consectetuer adipiscing elit, sed diam</p>
  <div class="abs" style="left:0;top:105px;width:143px;height:49px;background:var(--ink)"></div>
  <div class="dot dark" style="left:14px;top:60px"><svg viewBox="0 0 10 10"><circle cx="5" cy="4.5" r="2.5" fill="none" stroke="#fff" stroke-width="1"/><rect x="4" y="7.2" width="2" height="1.5" fill="#fff"/></svg></div>
  <p class="item-text" style="left:33px;top:59px;width:85px">Lorem ipsum dolor sit amet, consectetuer adipiscing elit, sed diam nonummy nibh euismod tincidunt ut laoreet</p>
  <div class="dot red" style="left:14px;top:85px"><svg viewBox="0 0 10 10"><path d="M5 1.5 8 2.8v2.4C8 7 6.7 8.2 5 8.8 3.3 8.2 2 7 2 5.2V2.8z" fill="none" stroke="#fff" stroke-width="1"/></svg></div>
  <p class="item-text" style="left:33px;top:84px;width:85px">Lorem ipsum dolor sit amet, consectetuer adipiscing elit, sed diam nonummy nibh euismod tincidunt ut laoreet</p>
  <div class="dot" style="left:14px;top:109px"><svg viewBox="0 0 10 10"><rect x="1.5" y="2" width="5" height="3.5" rx="1" fill="none" stroke="#fff" stroke-width=".8"/><rect x="3.5" y="4.5" width="5" height="3.5" rx="1" fill="none" stroke="#fff" stroke-width=".8"/></svg></div>
  <p class="item-text" style="left:33px;top:108px;width:85px;color:#d8d8da">Lorem ipsum dolor sit amet, consectetuer adipiscing elit, sed diam nonummy nibh euismod tincidunt ut laoreet</p>
  <div class="dot red" style="left:14px;top:131px"><svg viewBox="0 0 10 10"><circle cx="3" cy="4" r="1.3" fill="#fff"/><circle cx="7" cy="4" r="1.3" fill="#fff"/><circle cx="5" cy="3.3" r="1.5" fill="#fff"/><path d="M1.5 8c0-2 7-2 7 0z" fill="#fff"/></svg></div>
  <p class="item-text" style="left:33px;top:131px;width:85px;color:#d8d8da">Lorem ipsum dolor sit amet, consectetuer adipiscing elit, sed diam nonummy nibh euismod tincidunt ut laoreet</p>
  <div class="logo-mini" style="color:#c9a45a">LOGO</div>
</section>

<!-- Slide: figures -->
<section class="slide" style="left:474px;top:497px">
  <div class="photo" role="img" aria-label="Businessman in a blue suit signing a contract at a desk" style="left:146px;top:0;width:157px;height:170px;background:linear-gradient(150deg,#2d4d8e,#5b4536 45%,#d9d8d4 75%)"></div>
  <div class="title-red abs" style="left:16px;top:28px">This is a header<br>This is a header<br>This is a header</div>
  <p class="body abs" style="left:16px;top:66px;width:124px">Lorem ipsum dolor sit amet, consectetuer adipiscing elit, sed diam nonummy nibh euismod tincidunt ut laoreet dolore magna aliquam erat vo-</p>
  <svg class="abs" style="left:16px;top:110px;width:12px;height:12px" viewBox="0 0 12 12"><circle cx="6" cy="4" r="2.4" fill="none" stroke="var(--red)" stroke-width=".9"/><path d="M1 10.5c2-1.5 4-1.5 5 0s3 .5 5-1" fill="none" stroke="var(--red)" stroke-width=".9"/></svg>
  <div class="abs" style="left:33px;top:110px;font-size:6px;font-weight:700;color:var(--ink)">+120 000</div>
  <p class="item-text" style="left:33px;top:118px;width:70px;color:var(--muted)">Lorem ipsum dolor sit amet, consectetuer adipiscing elit, sed diam</p>
  <svg class="abs" style="left:16px;top:137px;width:13px;height:12px" viewBox="0 0 13 12"><path d="M1 5l3-3 2.5 2 2.5-2 3 3-5.5 5z" fill="none" stroke="var(--red)" stroke-width=".9"/></svg>
  <div class="abs" style="left:33px;top:137px;font-size:6px;font-weight:700;color:var(--ink)">+120 000</div>
  <p class="item-text" style="left:33px;top:145px;width:70px;color:var(--muted)">Lorem ipsum dolor sit amet, consectetuer adipiscing elit, sed diam</p>
  <div class="logo-mini">LOGO</div>
</section>

<!-- Slide: security -->
<section class="slide" style="left:829px;top:497px">
  <div class="photo" role="img" aria-label="Combination padlock resting on a laptop keyboard" style="left:0;top:0;width:128px;height:170px;background:linear-gradient(150deg,#5a6169,#2d3136 55%,#15171a)"></div>
  <div class="title-red abs" style="left:142px;top:16px">This is a header<br>This is a header</div>
  <p class="body abs" style="left:142px;top:39px;width:118px">Lorem ipsum dolor sit amet, consectetuer adipiscing elit, sed diam nonummy nibh euismod tincidunt ut laoreet dolore magna aliquam erat volutpat. Ut wisi enim ad minim veniam, quis nostrud exerci tation ullamcorper suscipit lobortis nisl ut aliquip ex ea com-</p>
  <div class="dot red" style="left:143px;top:92px"><svg viewBox="0 0 10 10"><circle cx="5" cy="4.5" r="2.5" fill="none" stroke="#fff" stroke-width="1"/><rect x="4" y="7.2" width="2" height="1.5" fill="#fff"/></svg></div>
  <div class="dot dark" style="left:169px;top:92px"><svg viewBox="0 0 10 10"><path d="M5 1.5 8 2.8v2.4C8 7 6.7 8.2 5 8.8 3.3 8.2 2 7 2 5.2V2.8z" fill="none" stroke="#fff" stroke-width="1"/></svg></div>
  <div class="dot red" style="left:199px;top:92px"><svg viewBox="0 0 10 10"><rect x="1.5" y="2" width="5" height="3.5" rx="1" fill="none" stroke="#fff" stroke-width=".8"/><rect x="3.5" y="4.5" width="5" height="3.5" rx="1" fill="none" stroke="#fff" stroke-width=".8"/></svg></div>
  <div class="dot dark" style="left:231px;top:91px"><svg viewBox="0 0 10 10"><circle cx="3" cy="4" r="1.3" fill="#fff"/><circle cx="7" cy="4" r="1.3" fill="#fff"/><circle cx="5" cy="3.3" r="1.5" fill="#fff"/><path d="M1.5 8c0-2 7-2 7 0z" fill="#fff"/></svg></div>
  <p class="abs" style="left:142px;top:122px;width:122px;font-size:4.6px;line-height:6px;font-weight:700;color:var(--ink)">Lorem ipsum dolor sit amet, consectetuer adipiscing elit, sed diam nonummy nibh euismod tincidunt ut laoreet dolore magna</p>
  <div class="logo-mini">LOGO</div>
</section>

<!-- Slide: text with points -->
<section class="slide" style="left:95px;top:723px">
  <div class="title-red abs" style="left:14px;top:34px">This is a header<br>This is a header</div>
  <p class="body abs" style="left:14px;top:56px;width:118px;font-size:4.3px;line-height:5.4px">Lorem ipsum dolor sit amet, consectetuer adipiscing elit, sed diam nonummy nibh euismod tincidunt ut laoreet dolore magna aliquam erat volutpat. Ut wisi enim ad minim veniam, quis nostrud exerci tation ullamcorper suscipit lobortis nisl ut aliquip ex ea commodo consequat. Duis autem vel eum iriure dolor in hendrerit in vulputate velit esse molestie consequat, vel illum dolore eu feugiat nulla facilisis at vero eros et accumsan et iusto<br><br>dignissim qui blandit praesent luptatum zzril delenit augue duis dolore te feugait nulla facilisi. Lorem ipsum dolor sit amet, cons ectetuer adipisc-</p>
  <div class="dot red" style="left:166px;top:45px"><svg viewBox="0 0 10 10"><circle cx="5" cy="4.5" r="2.5" fill="none" stroke="#fff" stroke-width="1"/><rect x="4" y="7.2" width="2" height="1.5" fill="#fff"/></svg></div>
  <div class="abs" style="left:185px;top:38px;font-size:4.6px;font-weight:700;color:var(--red)">THIS IS A HEADER</div>
  <p class="item-text" style="left:185px;top:45px;width:78px">Lorem ipsum dolor sit amet, consectetuer adipiscing elit, sed diam nonummy nibh euismod tincidunt ut</p>
  <div class="dot red" style="left:192px;top:87px"><svg viewBox="0 0 10 10"><path d="M5 1.5 8 2.8v2.4C8 7 6.7 8.2 5 8.8 3.3 8.2 2 7 2 5.2V2.8z" fill="none" stroke="#fff" stroke-width="1"/></svg></div>
  <div class="abs" style="left:210px;top:80px;font-size:4.6px;font-weight:700;color:var(--red)">THIS IS A HEADER</div>
  <p class="item-text" style="left:210px;top:87px;width:80px">Lorem ipsum dolor sit amet, consectetuer adipiscing elit, sed diam nonummy nibh euismod tincidunt ut</p>
  <div class="dot red" style="left:166px;top:121px"><svg viewBox="0 0 10 10"><circle cx="5" cy="4.5" r="2.5" fill="none" stroke="#fff" stroke-width="1"/><rect x="4" y="7.2" width="2" height="1.5" fill="#fff"/></svg></div>
  <div class="abs" style="left:187px;top:114px;font-size:4.6px;font-weight:700;color:var(--red)">THIS IS A HEADER</div>
  <p class="item-text" style="left:187px;top:121px;width:78px">Lorem ipsum dolor sit amet, consectetuer adipiscing elit, sed diam nonummy nibh euismod tincidunt ut</p>
  <div class="logo-mini">LOGO</div>
</section>

<!-- Slide: product with ticks -->
<section class="slide" style="left:474px;top:723px">
  <div class="photo" role="img" aria-label="Glass fragrance bottle beside a glass cloche on a stone surface" style="left:191px;top:0;width:112px;height:170px;background:linear-gradient(160deg,#c6c8cb,#6f7377 50%,#2f3134)"></div>
  <div class="title-red abs" style="left:16px;top:16px">This is a header<br>This is a header</div>
  <p class="body abs" style="left:16px;top:40px;width:118px">Lorem ipsum dolor sit amet, consectetuer adipiscing elit, sed diam nonummy nibh euismod tincidunt ut laoreet dolore magna aliquam erat volutpat. Ut wisi enim ad minim veniam, quis nostrud exerci tation ullamcorper suscipit lobortis nisl ut aliquip ex ea com-</p>
  <div class="abs" style="left:0;top:85px;width:191px;height:60px;background:var(--ink)"></div>
  <div class="tick" style="left:15px;top:101px"></div>
  <p class="item-text" style="left:27px;top:98px;width:72px;color:#cfd0d3">Lorem ipsum dolor sit amet, consectetuer adipiscing elit</p>
  <div class="tick" style="left:15px;top:114px"></div>
  <p class="item-text" style="left:27px;top:112px;width:72px;color:#cfd0d3">, sed diam nonummy nibh euismod tincidunt ut laoreet dolore mag</p>
  <div class="tick" style="left:15px;top:128px"></div>
  <p class="item-text" style="left:27px;top:126px;width:72px;color:#cfd0d3">na aliquam erat volutpat. Ut wisi enim ad minim veniam, quis nostrud</p>
  <div class="tick" style="left:110px;top:101px"></div>
  <p class="item-text" style="left:118px;top:98px;width:72px;color:#cfd0d3">Lorem ipsum dolor sit amet, consectetuer adipiscing elit</p>
  <div class="tick" style="left:110px;top:114px"></div>
  <p class="item-text" style="left:118px;top:112px;width:72px;color:#cfd0d3">, sed diam nonummy nibh euismod tincidunt ut laoreet dolore mag</p>
  <div class="tick" style="left:110px;top:128px"></div>
  <p class="item-text" style="left:118px;top:126px;width:72px;color:#cfd0d3">na aliquam erat volutpat. Ut wisi enim ad minim veniam, quis nostrud</p>
  <div class="logo-mini">LOGO</div>
</section>

<!-- Closing -->
<section class="slide" style="left:829px;top:723px">
  <div class="photo" role="img" aria-label="Laptop showing an analytics dashboard on a reflective desk" style="left:0;top:0;width:303px;height:172px;background:linear-gradient(160deg,#3b4660,#8f9aa8 40%,#4b4a4c 70%,#7a4b33)"></div>
  <div class="abs" style="left:10px;top:118px;font-size:12px;font-weight:700;color:var(--white)">THANK YOU</div>
  <div class="abs" style="left:10px;top:135px;font-size:25px;line-height:25px;font-weight:400;color:var(--white)">LOGO</div>
</section>

</body>
</html>
```